Postcard Design Project

Dental Practice Name: Marlow Ridge Dental (logo)Phone Number (310-555-0147) Front and backAddress (7815 N. Harwick Ave. Ste. B, Culver City, CA, 90230. (Back side only)General, Cosmetic, and Implant Dentistry Mention: Emergencies/Walk-ins Welcome, "Hablamos Espanol", Open Weekends Front Side:Promotions: 1. $75 New Patient Special including Exam, X-Rays, and Cleaning 2. Free Consultation 3. Accept all PPO Insurances Services: 1. Implant ($800) + Implant Crown/Abutment ($1200) -use photo of missing tooth 2. Clear Braces (starting at $2900) -use picture of clearvona teeth, cut out everything else and just use the before and after of the clearvona pictures 3. Whitening ($95) -use pic of whitened teeth 4. White fillings (starting at $95) -use pic of silver to white fillings) Back Side: 1. Picture of practice 2. picture of map with pin location 3. address and phone number
Dental

```html
<!DOCTYPE html>
<html lang="en">
<head>
<meta charset="utf-8">
<title>Marlow Ridge Dental Postcard</title>
<link href="https://fonts.googleapis.com/css2?family=Oswald:wght@500;600;700&family=Open+Sans:wght@400;600;700&display=swap" rel="stylesheet">
<style>
  :root {
    --navy: #1d5b86;
    --sky: #29b5e8;
    --yellow: #ffe81c;
    --red: #e3202d;
    --white: #ffffff;
    --photo-a: #d9e3ea;
    --photo-b: #9fb4c2;
  }
  * { margin: 0; padding: 0; box-sizing: border-box; }
  html, body { width: 789px; height: 1200px; overflow: hidden; background: var(--navy); }
  .postcard {
    position: relative; width: 789px; height: 1200px; overflow: hidden;
    background: var(--navy); font-family: "Open Sans", Arial, sans-serif; color: var(--white);
  }
  .backdrop { position: absolute; inset: 0; }
  .practice-name {
    position: absolute; left: 33px; top: 28px; white-space: nowrap;
    font-family: "Oswald", "Arial Narrow", sans-serif; font-weight: 600;
    font-size: 64px; line-height: 1.12; color: var(--navy); text-transform: uppercase;
  }
  .call-block { position: absolute; left: 528px; top: 30px; font-family: "Oswald", sans-serif; white-space: nowrap; }
  .call-label { font-size: 20px; font-weight: 500; letter-spacing: 0.5px; color: var(--white); }
  .call-phone { font-size: 38px; font-weight: 600; line-height: 1.05; color: var(--yellow); }
  .headline { position: absolute; left: 0; top: 0; width: 789px; height: 460px; font-family: "Oswald", sans-serif; text-transform: uppercase; }
  .headline > * { position: absolute; white-space: nowrap; line-height: 1; }
  .headline .emergencies { left: 357px; width: 402px; top: 205px; text-align: center; font-size: 37px; font-weight: 600; color: var(--yellow); }
  .headline .welcome { left: 357px; width: 402px; top: 246px; text-align: center; font-size: 104px; font-weight: 600; letter-spacing: -1px; }
  .headline .spanish { left: 357px; width: 402px; top: 364px; text-align: center; font-size: 36px; font-weight: 500; color: var(--sky); }
  .headline .weekends { right: 36px; top: 423px; font-family: "Open Sans", sans-serif; font-size: 21px; font-weight: 600; }
  .new-patient { position: absolute; left: 54px; top: 312px; display: flex; align-items: center; gap: 10px; }
  .new-patient .price { font-family: "Oswald", sans-serif; font-size: 56px; font-weight: 600; color: var(--yellow); line-height: 1; }
  .new-patient .details { font-size: 14px; line-height: 1.3; text-transform: uppercase; }
  .services { position: absolute; left: 465px; top: 470px; width: 293px; }
  .service { background: var(--yellow); padding: 0 4px 4px; margin-bottom: 24px; }
  .service h3 {
    font-family: "Oswald", sans-serif; font-weight: 600; font-size: 17px; line-height: 1.15;
    color: var(--red); text-align: center; text-transform: uppercase; padding: 6px 4px;
  }
  .service .results { display: flex; gap: 4px; }
  .result { position: relative; flex: 1; height: 88px; }
  .result .photo { position: absolute; inset: 0; }
  .result .tag {
    position: absolute; bottom: -4px; left: 50%; transform: translateX(-50%);
    width: 76px; padding: 2px 0; background: var(--sky); color: var(--navy);
    font-family: "Oswald", sans-serif; font-weight: 600; font-size: 18px; text-align: center; text-transform: uppercase;
  }
  .badge { position: absolute; left: 12px; top: 928px; width: 186px; height: 186px; }
  .address-bar {
    position: absolute; left: 0; top: 1118px; width: 789px; height: 82px; background: var(--yellow);
    display: flex; align-items: center; padding-left: 393px; gap: 10px; color: var(--navy);
  }
  .address-bar address { font-style: normal; font-size: 16px; font-weight: 600; line-height: 1.35; text-transform: uppercase; }
</style>
</head>
<body>
<main class="postcard">
  <svg class="backdrop" width="789" height="1200" viewBox="0 0 789 1200">
    <defs>
      <linearGradient id="photoTone" x1="0" y1="0" x2="1" y2="1">
        <stop offset="0" stop-color="var(--photo-a)"/>
        <stop offset="1" stop-color="var(--photo-b)"/>
      </linearGradient>
    </defs>
    <path d="M0,0 H472 V155 C300,190 150,235 0,300 Z" fill="var(--yellow)"/>
    <path d="M0,300 C150,235 300,190 472,155 C580,132 690,102 789,88 L789,118 C690,132 580,162 472,186 C300,222 150,268 0,330 Z" fill="var(--sky)"/>
    <path d="M0,440 C120,400 260,395 330,420 C400,450 420,520 410,600 C395,720 440,800 445,900 C450,1000 420,1060 400,1118 L0,1118 Z" fill="var(--sky)"/>
    <path role="img" aria-label="Photo of a dentist in a white cap examining a smiling young girl" d="M0,458 C120,420 255,414 322,437 C385,465 400,525 392,600 C378,720 422,800 427,900 C432,990 405,1050 385,1118 L0,1118 Z" fill="url(#photoTone)"/>
  </svg>

  <h1 class="practice-name">Marlow Ridge<br>Dental</h1>

  <div class="call-block">
    <div class="call-label">CALL US TODAY</div>
    <div class="call-phone">310-555-0147</div>
  </div>

  <div class="new-patient">
    <span class="price">$75</span>
    <span class="details">New patient special<br>including exam,<br>x-rays, and cleaning</span>
  </div>

  <section class="headline">
    <div class="emergencies">Emergencies/Walk-ins</div>
    <div class="welcome">Welcome</div>
    <div class="spanish">“Hablamos Espanol”</div>
    <div class="weekends">Open Weekends</div>
  </section>

  <section class="services">
    <article class="service">
      <h3>Implant $800 +<br>Implant Crown/Abutment $1200</h3>
      <div class="results">
        <div class="result"><div class="photo" role="img" aria-label="Smile with a missing front tooth" style="background:linear-gradient(#b8505a,#e8d9cf)"></div><span class="tag">Before</span></div>
        <div class="result"><div class="photo" role="img" aria-label="Smile with implant crown in place" style="background:linear-gradient(#c96b70,#f1ebe3)"></div><span class="tag">After</span></div>
      </div>
    </article>
    <article class="service">
      <h3>Whitening $95</h3>
      <div class="results">
        <div class="result"><div class="photo" role="img" aria-label="Yellowed teeth before whitening" style="background:linear-gradient(#c98a80,#e9dcc0)"></div><span class="tag">Before</span></div>
        <div class="result"><div class="photo" role="img" aria-label="Bright white teeth after whitening" style="background:linear-gradient(#d79a92,#f7f5f2)"></div><span class="tag">After</span></div>
      </div>
    </article>
    <article class="service">
      <h3>White Fillings Starting at $95</h3>
      <div class="results">
        <div class="result"><div class="photo" role="img" aria-label="Molars with silver fillings" style="background:linear-gradient(#8d8a88,#d8d2c8)"></div><span class="tag">Before</span></div>
        <div class="result"><div class="photo" role="img" aria-label="Molars with tooth-coloured fillings" style="background:linear-gradient(#c9bfb2,#efe9df)"></div><span class="tag">After</span></div>
      </div>
    </article>
    <article class="service">
      <h3>Clear Braces Starting at $2900</h3>
      <div class="results">
        <div class="result"><div class="photo" role="img" aria-label="Gapped teeth before clear aligner treatment" style="background:linear-gradient(#d46a7c,#efe3dc)"></div><span class="tag">Before</span></div>
        <div class="result"><div class="photo" role="img" aria-label="Straight teeth after clear aligner treatment" style="background:linear-gradient(#d97a88,#f3ece6)"></div><span class="tag">After</span></div>
      </div>
    </article>
  </section>

  <svg class="badge" viewBox="0 0 180 180">
    <defs><path id="badgeArc" d="M24,116 A71,71 0 0 1 126,29"/></defs>
    <circle cx="90" cy="90" r="88" fill="var(--white)"/>
    <circle cx="90" cy="90" r="83" fill="var(--red)"/>
    <g fill="var(--white)" font-family="Oswald, sans-serif" font-weight="600" text-anchor="middle">
      <text font-size="12.5" letter-spacing="0.3"><textPath href="#badgeArc" startOffset="50%">ACCEPT ALL PPO INSURANCES</textPath></text>
      <g transform="rotate(-20 98 115)">
        <text x="100" y="114" font-size="46" font-weight="700">FREE</text>
        <text x="100" y="136" font-size="17">CONSULTATION</text>
      </g>
    </g>
  </svg>

  <footer class="address-bar">
    <svg width="20" height="28" viewBox="0 0 20 28" aria-hidden="true">
      <path d="M10,0 C4.5,0 0,4.4 0,9.8 C0,17 10,28 10,28 C10,28 20,17 20,9.8 C20,4.4 15.5,0 10,0 Z" fill="var(--red)"/>
      <circle cx="10" cy="10" r="3.8" fill="var(--yellow)"/>
    </svg>
    <address>7815 N. Harwick Ave. Ste. B,<br>Culver City, CA, 90230</address>
  </footer>
</main>
</body>
</html>
```